Updated Buisness card/Design

Target Market(s)

Residential clients

Industry/Entity Type

Interior remodeling

Contact Information for Business Card

see mark up

Requirements
Must have
• Logo

```html
<!DOCTYPE html>
<html lang="en">
<head>
<meta charset="utf-8">
<title>Palmera Building Company – Business Card</title>
<link href="https://fonts.googleapis.com/css2?family=Montserrat:wght@400;500;600&family=Oswald:wght@500&display=swap" rel="stylesheet">
<style>
  :root {
    --brand-blue: #00a9f9;
    --brand-blue-deep: #0097e6;
    --ink: #3c3c3c;
    --slate: #8a949c;
    --paper: #ffffff;
    --backdrop: #e9ecef;
  }
  * { box-sizing: border-box; margin: 0; padding: 0; }
  html, body {
    width: 1200px; height: 1200px; overflow: hidden;
    background: var(--backdrop);
    font-family: "Montserrat", sans-serif;
  }
  .sheet {
    width: 1200px; height: 1200px;
    display: flex; align-items: center; justify-content: center; gap: 80px;
  }
  .card {
    position: relative;
    width: 420px; height: 735px;
    border-radius: 42px;
    overflow: hidden;
    box-shadow: 0 10px 30px rgba(0,0,0,0.12);
  }

  /* Front */
  .card-front { background: var(--paper); }
  .card-front .edge-band {
    position: absolute; left: 0; top: 0; bottom: 0; width: 26px;
    background: var(--brand-blue);
  }
  .card-front .brand {
    position: absolute; top: 70px; left: 26px; right: 0;
    display: flex; align-items: center; justify-content: center; gap: 12px;
  }
  .brand-square {
    width: 22px; height: 22px; background: var(--brand-blue);
  }
  .brand-name {
    font-weight: 600; font-size: 19px; letter-spacing: 1.5px;
    text-transform: uppercase; color: var(--slate); line-height: 1.25;
  }
  .person-name {
    position: absolute; left: 80px; top: 372px;
    font-weight: 500; font-size: 44px; color: var(--ink);
  }
  .contact {
    position: absolute; left: 110px; top: 470px; right: 20px;
    color: var(--ink); font-size: 17px; line-height: 1.35;
  }
  .contact-group { margin-bottom: 14px; }
  .contact-rule {
    width: 90px; height: 3px; background: var(--brand-blue);
    margin: 0 0 12px -6px;
  }

  /* Back */
  .card-back { background: var(--brand-blue); }
  .card-back .brand {
    position: absolute; top: 400px; left: 0; right: 0;
    display: flex; align-items: center; justify-content: center; gap: 12px;
  }
  .card-back .brand-square { background: var(--paper); }
  .card-back .brand-name { color: var(--paper); }
  .services {
    position: absolute; left: 20px; right: 20px; bottom: 90px;
    font-family: "Oswald", sans-serif; font-weight: 500;
    text-transform: uppercase; color: var(--paper);
    font-size: 13px; letter-spacing: 0.3px; line-height: 1.7;
    text-align: center;
  }
</style>
</head>
<body>
  <main class="sheet">
    <section class="card card-front" aria-label="Card front">
      <div class="edge-band"></div>
      <div class="brand">
        <span class="brand-square"></span>
        <span class="brand-name">Palmera Building<br>Company</span>
      </div>
      <h1 class="person-name">Daniel Reyes</h1>
      <div class="contact">
        <div class="contact-group">
          <p>Office - 555.014.2201</p>
          <p>Cell - 555.014.3390</p>
          <p>daniel@palmerabuilding.com</p>
        </div>
        <div class="contact-rule"></div>
        <div class="contact-group">
          <p>CA Contractors License - 512837</p>
        </div>
        <div class="contact-rule"></div>
        <div class="contact-group">
          <p>48 Harbor View Rd Suite 210</p>
          <p>Alder Bay, CA 90000</p>
        </div>
        <div class="contact-rule"></div>
        <div class="contact-group">
          <p>www.palmerabuilding.com</p>
        </div>
      </div>
    </section>

    <section class="card card-back" aria-label="Card back">
      <div class="brand">
        <span class="brand-square"></span>
        <span class="brand-name">Palmera Building<br>Company</span>
      </div>
      <div class="services">
        <p>Design-Build Services • Project Management • Kitchen &amp; Remodeling</p>
        <p>Specialty Services: Cabinets • Carpentry • Flooring • Tile • Stone</p>
      </div>
    </section>
  </main>
</body>
</html>
```